Delphine Marchetti Photography
Letterhead & Business Card Design
Delphine Marchetti Photography - Photography
Creative Brief
Professional
Delphine Marchetti
Photographer / Owner
517 Bramble Lane Fort McMurray, AB T9K 2P6
delphinemarchettiphotography@pixmail.example
www.delphinemarchettiphotography.example
I think I'd like to include a photo I've taken...thoughts?

```html
<!DOCTYPE html>
<html lang="en">
<head>
<meta charset="utf-8">
<title>Delphine Marchetti Photography – Business Cards</title>
<link href="https://fonts.googleapis.com/css2?family=Open+Sans:wght@400;600&display=swap" rel="stylesheet">
<style>
  :root {
    --bg: #2b2b2d;
    --card: #ffffff;
    --teal: #2a9fc9;
    --brown: #6b4a3a;
    --text: #4d4d4d;
    --muted: #8a8a8a;
    --rule: #cfcfcf;
  }
  * { box-sizing: border-box; margin: 0; padding: 0; }
  html, body { width: 1200px; height: 852px; overflow: hidden; }
  body {
    background: var(--bg);
    font-family: "Open Sans", Arial, sans-serif;
    color: var(--text);
    position: relative;
  }
  .card {
    position: absolute;
    width: 560px;
    height: 320px;
    background: var(--card);
    border-radius: 18px;
  }
  .card--front { left: 60px; top: 70px; }
  .card--back { left: 580px; top: 460px; }

  .brand { display: flex; align-items: center; gap: 14px; }
  .brand__dot {
    width: 70px; height: 70px; border-radius: 50%;
    background: var(--teal); flex: none;
  }
  .brand__name {
    font-size: 21px; font-weight: 400; color: var(--brown);
    line-height: 1.25; letter-spacing: 0.5px;
  }

  .person__name { font-size: 15px; font-weight: 600; color: var(--teal); }
  .person__role { font-size: 11px; color: var(--muted); margin-top: 2px; }
  .person__address { font-size: 11px; line-height: 1.5; margin-top: 10px; }

  .contact { list-style: none; font-size: 10.5px; }
  .contact li { display: flex; align-items: center; gap: 8px; height: 19px; }
  .contact svg { width: 11px; height: 11px; flex: none; fill: var(--teal); }

  .divider { position: absolute; width: 1px; background: var(--rule); }

  /* front card */
  .card--front .brand { position: absolute; left: 34px; top: 44px; }
  .card--front .person { position: absolute; left: 34px; top: 168px; width: 220px; text-align: right; }
  .card--front .divider { left: 268px; top: 168px; height: 96px; }
  .card--front .contact { position: absolute; left: 282px; top: 170px; }

  /* back card */
  .card--back .brand {
    position: absolute; left: 28px; top: 70px; width: 200px;
    flex-direction: column; text-align: center; gap: 12px;
  }
  .card--back .brand__name { font-size: 18px; }
  .card--back .divider { left: 236px; top: 60px; height: 200px; }
  .card--back .person { position: absolute; left: 254px; top: 62px; }
  .card--back .contact { position: absolute; left: 254px; top: 176px; }
</style>
</head>
<body>

<section class="card card--front" aria-label="Business card, front">
  <div class="brand">
    <span class="brand__dot"></span>
    <span class="brand__name">Delphine Marchetti<br>Photography</span>
  </div>
  <div class="person">
    <p class="person__name">Delphine Marchetti</p>
    <p class="person__role">Photographer / Owner</p>
    <p class="person__address">517 Bramble Lane<br>Fort McMurray, AB T9K 2P6</p>
  </div>
  <span class="divider"></span>
  <ul class="contact">
    <li><svg viewBox="0 0 12 12"><path d="M2.5 1l2 2.2-1 1.3a7 7 0 0 0 4 4l1.3-1 2.2 2-1.3 1.5C5.5 11 1 6.5 1 2.3z"/></svg>780.555.0142</li>
    <li><svg viewBox="0 0 12 12"><path d="M3 0h6a1 1 0 0 1 1 1v10a1 1 0 0 1-1 1H3a1 1 0 0 1-1-1V1a1 1 0 0 1 1-1zm0 1.5v8h6v-8z"/></svg>780.555.0187</li>
    <li><svg viewBox="0 0 12 12"><circle cx="6" cy="6" r="6"/><circle cx="6" cy="6" r="2" fill="#fff"/></svg>delphinemarchettiphotography@pixmail.example</li>
    <li><svg viewBox="0 0 12 12"><circle cx="6" cy="6" r="6"/><path d="M1 6h10M6 1v10" stroke="#fff" stroke-width="1"/></svg>www.delphinemarchettiphotography.example</li>
  </ul>
</section>

<section class="card card--back" aria-label="Business card, back">
  <div class="brand">
    <span class="brand__dot"></span>
    <span class="brand__name">Delphine Marchetti<br>Photography</span>
  </div>
  <span class="divider"></span>
  <div class="person">
    <p class="person__name">Delphine Marchetti</p>
    <p class="person__role">Photographer / Owner</p>
    <p class="person__address">517 Bramble Lane<br>Fort McMurray, AB T9K 2P6</p>
  </div>
  <ul class="contact">
    <li><svg viewBox="0 0 12 12"><path d="M2.5 1l2 2.2-1 1.3a7 7 0 0 0 4 4l1.3-1 2.2 2-1.3 1.5C5.5 11 1 6.5 1 2.3z"/></svg>780.555.0142</li>
    <li><svg viewBox="0 0 12 12"><path d="M3 0h6a1 1 0 0 1 1 1v10a1 1 0 0 1-1 1H3a1 1 0 0 1-1-1V1a1 1 0 0 1 1-1zm0 1.5v8h6v-8z"/></svg>780.555.0187</li>
    <li><svg viewBox="0 0 12 12"><circle cx="6" cy="6" r="6"/><circle cx="6" cy="6" r="2" fill="#fff"/></svg>delphinemarchettiphotography@pixmail.example</li>
    <li><svg viewBox="0 0 12 12"><circle cx="6" cy="6" r="6"/><path d="M1 6h10M6 1v10" stroke="#fff" stroke-width="1"/></svg>www.delphinemarchettiphotography.example</li>
  </ul>
</section>

</body>
</html>
```